Banner

I need a banner made showcasing our products and USPs! I have attached a design that was done in-house but not very good so looking for a better design

Industry/Entity Type

Fintech

```html
<!DOCTYPE html>
<html lang="en">
<head>
<meta charset="utf-8">
<title>Keelpay Merchant Services – Banner</title>
<link href="https://fonts.googleapis.com/css2?family=Roboto:wght@400;500;700&family=Roboto+Slab:wght@700&display=swap" rel="stylesheet">
<style>
  :root{
    --navy:#0b4a8a;
    --blue:#1565b8;
    --royal:#2e3f9e;
    --orange:#f08a1c;
    --ink:#222;
    --grey:#555;
    --band:#e6e6e6;
    --line:#2e3f9e;
  }
  html,body{margin:0;padding:0;width:1200px;height:1200px;overflow:hidden;background:#fff;font-family:"Roboto",sans-serif;}
  .banner{position:absolute;left:319px;top:38px;width:562px;height:1124px;background:#fff;box-shadow:0 0 14px rgba(60,70,140,.35);overflow:hidden;}
  .abs{position:absolute;}
  .brand{left:351px;top:14px;width:190px;text-align:right;}
  .brand-name{font-size:40px;font-weight:700;color:var(--navy);line-height:1;letter-spacing:-0.5px;}
  .brand-sub{font-size:12px;color:var(--grey);margin-top:2px;}
  .headline-lead{left:30px;top:382px;font-size:29px;color:var(--orange);}
  .headline-band{left:23px;top:418px;}
  .headline-main{left:32px;top:419px;font-size:38px;color:#fff;line-height:42px;}
  .headline-main b{font-weight:700;}
  .tagline{left:28px;top:467px;font-size:18px;color:var(--grey);letter-spacing:.3px;}
  .offer{left:34px;top:525px;width:200px;height:180px;}
  .offer-text{left:50px;top:550px;width:104px;text-align:center;color:var(--ink);font-size:11px;line-height:15px;}
  .offer-text .any{display:block;font-size:34px;font-weight:700;color:var(--orange);line-height:36px;}
  .usp{left:99px;font-family:"Roboto Slab",serif;font-weight:700;font-size:14px;color:var(--blue);}
  .usp-icon{left:42px;width:30px;height:30px;}
  .rule{left:98px;width:252px;height:1px;background:var(--line);}
  .service{width:122px;height:122px;}
  .service-label{width:122px;text-align:center;font-family:"Roboto Slab",serif;font-weight:700;font-size:14px;line-height:18px;color:var(--navy);}
  .footer{left:0;top:1056px;width:562px;height:68px;background:var(--band);}
  .pattern{left:0;top:0;}
</style>
</head>
<body>
<div class="banner">

  <svg class="abs pattern" width="330" height="370" viewBox="0 0 330 370">
    <defs>
      <linearGradient id="patternTone" x1="0" y1="0" x2="1" y2="1">
        <stop offset="0" stop-color="#1a6f9e"/>
        <stop offset=".35" stop-color="#f0582e"/>
        <stop offset=".65" stop-color="#f39a2e"/>
        <stop offset="1" stop-color="#0b4a8a"/>
      </linearGradient>
    </defs>
    <polygon role="img" aria-label="Geometric triangle mosaic in orange, red, teal and navy" points="0,0 308,0 256,60 208,88 208,236 176,258 140,238 52,276 0,268" fill="url(#patternTone)"/>
    <polygon points="258,0 308,0 308,30" fill="#f0482e"/>
    <polygon points="240,180 240,206 222,194" fill="#f07a2e"/>
    <polygon points="208,236 256,262 208,278" fill="#fbc98a"/>
    <polygon points="102,298 102,346 51,322" fill="var(--navy)"/>
    <polygon points="69,345 83,353 69,361" fill="var(--navy)"/>
  </svg>

  <div class="abs brand">
    <div class="brand-name">Keelpay</div>
    <div class="brand-sub">Merchant Services</div>
  </div>

  <svg class="abs" style="left:230px;top:80px" width="330" height="320" viewBox="230 80 330 320">
    <polygon points="395,83 552,240 395,397 238,240" fill="none" stroke="var(--orange)" stroke-width="2.4"/>
    <polygon points="412,110 542,240 412,370 282,240" fill="none" stroke="var(--navy)" stroke-width="2.4"/>
    <rect role="img" aria-label="Photo of a finger pressing a shopping cart button surrounded by small web icons" x="333" y="160" width="180" height="136" rx="16" fill="#e9eef5"/>
  </svg>

  <div class="abs headline-lead">Cutting Your</div>
  <svg class="abs headline-band" width="400" height="44" viewBox="0 0 400 44"><polygon points="0,0 340,0 396,42 0,42" fill="var(--navy)"/></svg>
  <div class="abs headline-main">Transaction <b>Costs</b></div>
  <div class="abs tagline">INNOVATIVE PAYMENT SOLUTIONS</div>

  <svg class="abs offer" viewBox="34 525 200 180">
    <circle cx="141" cy="594" r="68" fill="var(--royal)"/>
    <polygon points="102,527 196,527 209,594" fill="var(--royal)"/>
    <circle cx="102" cy="585" r="58" fill="#fff" stroke="var(--royal)" stroke-width="3"/>
    <circle cx="156" cy="532" r="4" fill="var(--orange)" stroke="#fff" stroke-width="1.5"/>
  </svg>
  <div class="abs offer-text">WE WILL BEAT<span class="any">ANY</span>LIKE FOR LIKE<br>QUOTE</div>

  <svg class="abs usp-icon" style="top:685px" viewBox="0 0 30 30"><rect x="14" y="2" width="12" height="14" rx="2" fill="var(--navy)"/><path d="M2 18h8l6 3h10v5H8l-6-2z" fill="none" stroke="var(--navy)" stroke-width="2"/></svg>
  <div class="abs usp" style="top:690px">SAME DAY/NEXT DAY FUNDING</div>
  <div class="abs rule" style="top:730px"></div>

  <svg class="abs usp-icon" style="top:744px" viewBox="0 0 30 30"><circle cx="11" cy="11" r="10" fill="var(--blue)"/><text x="11" y="15" font-size="10" fill="#fff" text-anchor="middle" font-family="Roboto,sans-serif">24</text><path d="M18 16l9 9-3 3-9-9z" fill="none" stroke="var(--navy)" stroke-width="1.6"/></svg>
  <div class="abs usp" style="top:751px">24 HOUR SWAP-OUT</div>
  <div class="abs rule" style="top:791px"></div>

  <svg class="abs usp-icon" style="top:810px" viewBox="0 0 30 30"><rect x="2" y="6" width="26" height="18" rx="2" fill="var(--navy)"/><rect x="16" y="12" width="10" height="6" rx="1" fill="#fff"/></svg>
  <div class="abs usp" style="top:814px">ORCHARD PAY &amp; GLEAM PAY ENABLE</div>
  <div class="abs rule" style="top:862px"></div>

  <svg class="abs usp-icon" style="top:882px" viewBox="0 0 30 30"><rect x="4" y="2" width="18" height="26" rx="2" fill="none" stroke="var(--grey)" stroke-width="1.6"/><rect x="8" y="6" width="10" height="10" fill="var(--blue)"/><path d="M16 20v8h8v-4z" fill="#fff" stroke="var(--navy)" stroke-width="1.4"/></svg>
  <div class="abs usp" style="top:888px">INTERGRATED EPOS SOLUTION</div>
  <div class="abs rule" style="top:930px"></div>

  <svg class="abs usp-icon" style="top:944px" viewBox="0 0 30 30"><circle cx="13" cy="3" r="2" fill="var(--navy)"/><ellipse cx="15" cy="17" rx="12" ry="9" fill="var(--navy)"/><rect x="7" y="22" width="4" height="6" fill="var(--navy)"/><rect x="18" y="22" width="4" height="6" fill="var(--navy)"/></svg>
  <div class="abs usp" style="top:952px">SAVE UO TO 40%</div>

  <svg class="abs" style="left:385px;top:634px" width="124" height="390" viewBox="385 634 124 390">
    <defs>
      <clipPath id="ringA"><circle cx="446" cy="695" r="57"/></clipPath>
      <clipPath id="ringB"><circle cx="446" cy="823" r="57"/></clipPath>
      <clipPath id="ringC"><circle cx="446" cy="953" r="57"/></clipPath>
    </defs>
    <g fill="none" stroke-width="2.4">
      <path d="M388 695a58 58 0 0 1 116 0" stroke="var(--orange)"/><path d="M504 695a58 58 0 0 1-116 0" stroke="var(--royal)"/>
      <path d="M388 823a58 58 0 0 1 116 0" stroke="var(--orange)"/><path d="M504 823a58 58 0 0 1-116 0" stroke="var(--royal)"/>
      <path d="M388 953a58 58 0 0 1 116 0" stroke="var(--orange)"/><path d="M504 953a58 58 0 0 1-116 0" stroke="var(--royal)"/>
    </g>
    <rect role="img" aria-label="Photo of an EPOS till with touchscreen and printer" clip-path="url(#ringA)" x="408" y="652" width="76" height="42" rx="6" fill="#d9dde3"/>
    <rect role="img" aria-label="Photo of bundles of banknotes" clip-path="url(#ringB)" x="408" y="780" width="76" height="40" rx="6" fill="#e8d8c8"/>
    <rect role="img" aria-label="Photo of a handheld card payment terminal" clip-path="url(#ringC)" x="420" y="900" width="52" height="44" rx="6" fill="#c9ccd1"/>
  </svg>
  <div class="abs service-label" style="left:385px;top:702px">EPOS<br>SYSTEMS</div>
  <div class="abs service-label" style="left:385px;top:826px">CASH<br>ADVANCE</div>
  <div class="abs service-label" style="left:385px;top:953px">CARD<br>PAYMENMTS</div>

  <div class="abs footer"></div>
  <svg class="abs" style="left:140px;top:1074px" width="284" height="26" viewBox="0 0 284 26">
    <ellipse cx="20" cy="12" rx="19" ry="11" fill="none" stroke="#444" stroke-width="1"/>
    <rect x="47" y="1" width="34" height="22" rx="2" fill="#fff" stroke="#999"/>
    <rect x="87" y="1" width="34" height="22" rx="2" fill="#fff" stroke="#999"/>
    <rect x="127" y="1" width="34" height="22" rx="2" fill="#fff" stroke="#999"/>
    <rect x="167" y="1" width="34" height="22" rx="2" fill="#7b2e8e"/>
    <rect x="207" y="1" width="34" height="22" rx="2" fill="#2e3f9e"/>
    <rect x="247" y="1" width="34" height="22" rx="2" fill="#2e3f9e"/>
  </svg>

</div>
</body>
</html>
```